Facebook cover photo and profile picture for local trade construction quotation website

Hi,I need a Facebook design for a cover photo and profile picture ,to meet the new facebook design branding requirements which are:
Background cover photo image : 851 x 315 px JPEG
Profile picture : high quality image that scales well from 180 x 180 pixels to 32 x 32 pixels JPEG
The Facebook page is for my new website which is a trade quatation site, you can visit the website at www.bidnest.example to get a feel for the website. We would like the profile picture to be the name of the website ( bidnest.example) and to be in Orange and black as it is on the website, this will be in the centre of the picture feel free to have any colour background or add anything around the writing I am open to any ideas .
For the background cover photo, I am again open to any design idea , perhaps it should have a cartoon builder which you can use from the website homepage and have that somewhere in the design , and possibly have the website address www.bidnest.example and perhaps the email address which is enquiries@bidnest.example other than that please feel free to use your imagination I am looking for the WOW factor to attract people to the website.

Industry/Entity Type

Construction

```html
<!DOCTYPE html>
<html lang="en">
<head>
<meta charset="utf-8">
<title>bidnest.example – cover and profile</title>
<link rel="stylesheet" href="https://fonts.googleapis.com/css2?family=Cabin:wght@600&display=swap">
<style>
  :root {
    --paper: #f1ebe3;
    --paper-edge: #e8e0d6;
    --ink-brown: #3b2a24;
    --gold: #eab23a;
    --shadow: rgba(60, 45, 35, 0.45);
    --page: #ffffff;
    --builder-blue: #2f6fc4;
    --builder-yellow: #f3c02c;
  }
  * { margin: 0; padding: 0; box-sizing: border-box; }
  html, body {
    width: 1200px;
    height: 543px;
    overflow: hidden;
    background: var(--page);
  }
  .canvas {
    position: relative;
    width: 1200px;
    height: 543px;
    font-family: "Cabin", "Gill Sans", sans-serif;
  }
  .cover {
    position: absolute;
    left: 0; top: 0;
    width: 1200px;
    height: 443px;
    background:
      radial-gradient(ellipse at 50% 45%, var(--paper) 55%, var(--paper-edge) 100%);
  }
  .email-tag {
    position: absolute;
    left: 51px;
    top: 202px;
    height: 42px;
    padding: 0 13px;
    background: var(--ink-brown);
    color: var(--gold);
    font-size: 15px;
    line-height: 42px;
    letter-spacing: 0.2px;
  }
  .email-tag::after {
    content: "";
    position: absolute;
    left: 165px;
    bottom: -10px;
    border-left: 10px solid transparent;
    border-right: 10px solid transparent;
    border-top: 10px solid var(--ink-brown);
  }
  .shade-line {
    position: absolute;
    left: 380px;
    width: 440px;
    height: 14px;
    background: radial-gradient(ellipse at 50% 50%, var(--shadow) 0%, rgba(60,45,35,0.15) 45%, transparent 72%);
  }
  .shade-line.top { top: 100px; }
  .shade-line.bottom { top: 326px; }
  .wordmark {
    position: absolute;
    left: 300px;
    width: 600px;
    top: 172px;
    text-align: center;
    font-size: 72px;
    font-weight: 600;
    color: var(--ink-brown);
    line-height: 100px;
    letter-spacing: 1px;
  }
  .builder-art {
    position: absolute;
    left: 895px;
    top: 25px;
    width: 245px;
    height: 418px;
    border-radius: 40px 40px 12px 12px;
    background: linear-gradient(180deg, var(--builder-yellow) 0%, #f6e3c8 22%, var(--builder-blue) 45%, var(--builder-blue) 85%, var(--builder-yellow) 100%);
    opacity: 0.85;
  }
  .profile-picture {
    position: absolute;
    left: 40px;
    top: 303px;
    width: 226px;
    height: 226px;
    background: var(--paper);
    display: flex;
    align-items: center;
    justify-content: center;
  }
  .profile-picture .wordmark-small {
    font-size: 27px;
    font-weight: 600;
    color: var(--ink-brown);
    letter-spacing: 0.5px;
  }
</style>
</head>
<body>
  <div class="canvas">
    <section class="cover">
      <div class="email-tag">enquiries@bidnest.example</div>
      <div class="shade-line top"></div>
      <div class="wordmark">bidnest.example</div>
      <div class="shade-line bottom"></div>
      <div class="builder-art" role="img" aria-label="Cartoon builder in yellow hard hat and blue overalls giving two thumbs up"></div>
    </section>
    <section class="profile-picture">
      <span class="wordmark-small">bidnest.example</span>
    </section>
  </div>
</body>
</html>
```